Beauty website banner

We are an Australian beauty website selling mid and high end cosmetics and beauty products.

We need a banner that tells customers they can share their product wishlists with friends to let them know what they want for Christmas.

Target Market(s)

Female, 30-60, white collar

Industry/Entity Type

Cosmetics

Requirements
Must have
• 600 x 150 pixels in size

Words to be as follows, not including the (") of course.

"Share your wishlist with friends and family for Christmas!"

(Then in smaller font) "Just log in to your account, go to your wishlist and click on the ‘share wishlist’ button"

```html
<!DOCTYPE html>
<html lang="en">
<head>
<meta charset="utf-8">
<title>Share Your Wishlist for Christmas</title>
<link rel="stylesheet" href="https://fonts.googleapis.com/css2?family=Cinzel:wght@400;500&display=swap">
<style>
  :root {
    --silver-light: #ffffff;
    --silver-mid: #d9d9d9;
    --silver-deep: #9c9c9c;
    --silver-edge: #7d7d7d;
    --ink: #161616;
    --bauble-glow: #f4f4f4;
    --bauble-shade: #a8a8a8;
  }
  * { margin: 0; padding: 0; box-sizing: border-box; }
  html, body {
    width: 1200px;
    height: 300px;
    overflow: hidden;
    background: var(--silver-mid);
  }
  .banner {
    position: relative;
    width: 1200px;
    height: 300px;
    overflow: hidden;
    background:
      radial-gradient(ellipse 520px 260px at 560px 130px, var(--silver-light) 0%, rgba(255,255,255,0.6) 35%, rgba(255,255,255,0) 75%),
      linear-gradient(90deg, var(--silver-deep) 0%, var(--silver-mid) 22%, #ececec 48%, var(--silver-mid) 78%, var(--silver-edge) 100%);
    font-family: "Cinzel", "Times New Roman", serif;
    color: var(--ink);
  }
  .sparkle-trail {
    position: absolute;
    left: 0;
    top: 150px;
    width: 420px;
    height: 150px;
    background: radial-gradient(ellipse 200px 70px at 90px 110px, rgba(255,255,255,0.55), rgba(255,255,255,0) 80%);
  }
  .baubles {
    position: absolute;
    left: 820px;
    top: 0;
    width: 380px;
    height: 300px;
    background:
      radial-gradient(circle 70px at 120px 120px, var(--bauble-glow) 0%, #cfcfcf 60%, rgba(168,168,168,0) 100%),
      radial-gradient(circle 95px at 265px 185px, var(--bauble-glow) 0%, #cdcdcd 60%, rgba(168,168,168,0) 100%),
      radial-gradient(ellipse 220px 160px at 220px 150px, rgba(255,255,255,0.5), rgba(255,255,255,0) 80%);
  }
  .headline {
    position: absolute;
    left: 88px;
    top: 58px;
    font-size: 38px;
    font-weight: 500;
    line-height: 44px;
    letter-spacing: 0.5px;
  }
  .instructions {
    position: absolute;
    left: 88px;
    top: 190px;
    font-size: 21px;
    font-weight: 400;
    line-height: 25px;
    letter-spacing: 0.3px;
  }
</style>
</head>
<body>
  <main class="banner">
    <div class="sparkle-trail" role="img" aria-label="Swirling trail of white sparkles and stars"></div>
    <div class="baubles" role="img" aria-label="Two glossy silver Christmas baubles hanging on thin threads among sparkles and soft bokeh"></div>
    <h1 class="headline">Share your wishlist with friends<br>and family for Christmas!</h1>
    <p class="instructions">Just log in to your account, go to your wishlist<br>and click on the ‘share wishlist’ button</p>
  </main>
</body>
</html>
```